R5 Construction USA

We are General Contractors performing Federal Contracting two generations, website with one page our 'Capability Statement", five page website, want to as soon as possible secure page and Under Construction with R5 logo. No files to upload yet, time to assemble.

Coding

Coded - Design and coding required

Number of Pages Required

1 page

```html
<!DOCTYPE html>
<html lang="en">
<head>
<meta charset="UTF-8">
<title>R5 Construction USA — Under Construction</title>
<link rel="stylesheet" href="https://fonts.googleapis.com/css2?family=Chakra+Petch:wght@600;700&family=Inter:wght@400;500;600&display=swap">
<style>
  :root {
    --navy-deep: #0b2170;
    --navy: #1a2f8c;
    --violet: #3a2478;
    --magenta: #5a1f6a;
    --white: #ffffff;
    --muted: #d6dbef;
    --red: #c0102f;
    --red-text: #d4123a;
    --input-text: #4b4f5c;
  }
  * { margin: 0; padding: 0; box-sizing: border-box; }
  html, body { width: 1200px; height: 704px; overflow: hidden; }
  body {
    position: relative;
    font-family: "Inter", Arial, sans-serif;
    color: var(--white);
    background: var(--navy-deep);
  }
  .hero-backdrop {
    position: absolute; inset: 0;
    background:
      radial-gradient(ellipse at 85% 90%, rgba(110, 35, 105, 0.55), transparent 55%),
      radial-gradient(ellipse at 20% 35%, rgba(70, 45, 130, 0.45), transparent 55%),
      linear-gradient(180deg, #10287a 0%, #1b3a8e 45%, #243c8c 70%, #2a2c7e 100%);
  }
  .brand {
    position: absolute; left: 0; right: 0; top: 82px;
    display: flex; flex-direction: column; align-items: center;
  }
  .brand-circle {
    width: 104px; height: 104px; border-radius: 50%;
    border: 5px solid var(--white);
  }
  .brand-name {
    margin-top: 26px;
    font-family: "Chakra Petch", Arial, sans-serif;
    font-weight: 700; font-size: 18px; letter-spacing: 3px;
    color: var(--white);
  }
  .launch-badge {
    position: absolute; left: 492px; top: 303px;
    width: 216px; height: 31px; border-radius: 16px;
    border: 1px solid var(--red);
    background: rgba(60, 20, 70, 0.35);
    color: var(--red-text);
    font-size: 12px; display: flex; align-items: center; justify-content: center;
  }
  .headline {
    position: absolute; left: 0; right: 0; top: 356px;
    text-align: center;
    font-family: "Chakra Petch", Arial, sans-serif;
    font-weight: 700; font-size: 38px; letter-spacing: 0.3px;
  }
  .tagline {
    position: absolute; left: 0; right: 0; top: 408px;
    text-align: center; font-size: 17px; font-weight: 400;
  }
  .intro {
    position: absolute; left: 0; right: 0; top: 447px;
    text-align: center; font-size: 15px; color: var(--muted);
  }
  .signup {
    position: absolute; left: 362px; top: 501px;
    display: flex; gap: 17px;
  }
  .signup-input {
    width: 328px; height: 49px; border-radius: 8px; border: none;
    background: var(--white); padding: 0 19px;
    font-family: inherit; font-size: 15px; color: var(--input-text);
  }
  .signup-input::placeholder { color: var(--input-text); }
  .signup-button {
    width: 130px; height: 49px; border-radius: 8px; border: none;
    background: var(--red); color: var(--white);
    font-family: inherit; font-weight: 600; font-size: 15px;
  }
  .footer-links {
    position: absolute; left: 98px; top: 641px;
    display: flex; align-items: center; font-size: 12px;
  }
  .footer-links a { color: var(--white); text-decoration: none; }
  .footer-divider {
    width: 1px; height: 15px; background: var(--white); margin: 0 20px;
  }
  .copyright {
    position: absolute; right: 99px; top: 641px; font-size: 12px;
  }
</style>
</head>
<body>
  <div class="hero-backdrop" role="img" aria-label="City skyline with high-rise buildings and tower cranes under construction, tinted blue and purple"></div>

  <header class="brand">
    <div class="brand-circle"></div>
    <div class="brand-name">R5 CONSTRUCTION USA</div>
  </header>

  <div class="launch-badge">Website Launch Coming Soon</div>
  <h1 class="headline">UNDER CONSTRUCTION</h1>
  <p class="tagline">Two Generations of Excellence in Federal Contracting</p>
  <p class="intro">Our new website is being built. We're assembling something great — check back soon.</p>

  <form class="signup">
    <input class="signup-input" type="email" placeholder="Enter your email">
    <button class="signup-button" type="button">Subscribe</button>
  </form>

  <nav class="footer-links">
    <a href="#">Contact Us</a>
    <span class="footer-divider"></span>
    <a href="#">Email Us</a>
  </nav>
  <p class="copyright">© 2026 R5 Construction USA. All rights reserved.</p>
</body>
</html>
```